deceased estate clean ups brochures

we would like a brochure to reresent our business we already have new web site and want to do DL A4 brochure to give out to promote our business we already have logo www.larkmore.com.au is where you can get all info needed

Target Market(s)

families with loved ones that have past away
people done sizing or needing to decluter

Colors
cadf82
33b8a4
886aae
33a6d7

```html
<!DOCTYPE html>
<html lang="en">
<head>
<meta charset="utf-8">
<title>Larkmore – Deceased Estate Cleanups Brochure (Outside)</title>
<link rel="stylesheet" href="https://fonts.googleapis.com/css2?family=Cinzel:wght@400;500&family=Montserrat:ital,wght@0,400;0,500;0,600;1,400&display=swap">
<style>
  :root{
    --lime:#cadf82;
    --lime-deep:#a9c64a;
    --teal:#33b8a4;
    --purple:#886aae;
    --purple-deep:#6f52a0;
    --blue:#33a6d7;
    --ink:#2b2b2b;
    --paper:#f7f7f8;
    --stage:#3b3b3d;
  }
  *{box-sizing:border-box;margin:0;padding:0}
  html,body{width:802px;height:1200px;overflow:hidden;background:var(--stage)}
  body{font-family:"Montserrat",Arial,sans-serif;color:var(--ink)}
  .brochure{position:absolute;left:11px;top:299px;width:780px;height:602px;background:var(--paper);box-shadow:0 8px 24px rgba(0,0,0,.45);overflow:hidden}
  .shapes{position:absolute;inset:0}
  .panel{position:absolute;top:0;width:260px;height:602px;text-align:center}
  .panel--left{left:0}.panel--mid{left:260px}.panel--right{left:520px}
  .footer{position:absolute;left:0;bottom:0;width:260px;height:27px;line-height:27px;color:#fff;font-size:8.5px;letter-spacing:.8px}
  .footer--purple{background:var(--purple)}
  .footer--lime{background:var(--lime-deep)}

  .section-title{position:absolute;top:32px;left:0;width:260px;font-family:"Cinzel",serif;font-size:13px;color:var(--lime-deep)}
  .section-title span{color:var(--purple)}
  .feature{position:absolute;left:18px;width:224px}
  .feature__icon{display:block;margin:0 auto 4px;width:20px;height:20px}
  .feature__title{font-size:9px;font-weight:600;color:var(--teal);letter-spacing:.2px}
  .feature__text{font-size:7.3px;line-height:10.5px;margin-top:3px}

  .quote{position:absolute;left:18px;top:242px;width:224px;height:84px;border:1px dashed #c9c9cf;border-radius:10px}
  .quote__mark{position:absolute;left:0;right:0;top:-26px;font-family:Georgia,serif;font-size:50px;color:#b9a8d2;line-height:1}
  .quote__text{position:absolute;left:10px;right:10px;top:18px;font-size:7.4px;line-height:12px;font-style:italic}
  .quote__name{position:absolute;left:0;right:0;bottom:-6px;font-size:11px;font-weight:600;color:var(--purple)}
  .quote__name small{font-size:6px;font-weight:400;color:var(--ink);letter-spacing:.4px}
  .quote__name b{background:var(--paper);padding:0 6px;font-weight:600}

  .brand{font-family:"Cinzel",serif;font-weight:500;color:var(--ink);letter-spacing:1.5px}
  .brand-dot{display:block;margin:0 auto;border-radius:50%;background:var(--teal)}
  .contact-brand{position:absolute;top:358px;left:0;width:260px}
  .contact-brand .brand-dot{width:24px;height:24px;margin-bottom:8px}
  .contact-brand .brand{font-size:14px}
  .enquire{position:absolute;top:437px;left:0;width:260px;font-size:8.5px}
  .enquire strong{display:block;font-size:11.5px;font-weight:600;color:var(--ink);margin-top:2px}
  .enquire strong em{font-style:normal;color:var(--lime-deep)}
  .icons{position:absolute;top:478px;left:0;width:260px;display:flex;justify-content:center;gap:6px}
  .icons svg{width:14px;height:14px}
  .contact-lines{position:absolute;top:507px;left:0;width:260px;font-size:8.5px;line-height:12.5px}

  .right-brand{position:absolute;top:18px;left:0;width:260px}
  .right-brand .brand-dot{width:40px;height:40px;margin-bottom:12px}
  .right-brand .brand{font-size:23px}
  .tagline{position:absolute;top:425px;left:0;width:260px;font-size:11px;font-weight:500;color:var(--lime-deep);letter-spacing:.4px}
  .headline{position:absolute;top:443px;left:0;width:260px;font-family:"Cinzel",serif;line-height:1}
  .headline span{display:block;font-size:19.5px;letter-spacing:.5px}
  .headline strong{display:block;font-weight:400;font-size:33px;letter-spacing:1px;margin-top:2px}
  .intro{position:absolute;top:528px;left:22px;width:216px;font-size:7.6px;line-height:11.5px}
</style>
</head>
<body>
<main class="brochure">
  <svg class="shapes" viewBox="0 0 780 602" width="780" height="602" aria-hidden="true">
    <!-- left panel top wave -->
    <path d="M0 0H260V10C180 0 80 20 0 40Z" fill="var(--purple)"/>
    <path d="M0 46C80 26 180 8 260 14" fill="none" stroke="var(--lime)" stroke-width="3"/>
    <!-- left panel bottom wave -->
    <path d="M0 412C90 400 190 380 260 388" fill="none" stroke="var(--lime-deep)" stroke-width="3"/>
    <!-- middle top band -->
    <path d="M260 0H470V20C420 30 340 10 260 22Z" fill="var(--purple)" opacity=".85"/>
    <!-- right panel purple wave -->
    <path d="M470 0H780V100C700 140 620 135 520 110C500 60 490 20 470 0Z" fill="var(--purple)"/>
    <path d="M520 0H780V95C690 128 610 120 560 90C540 70 530 30 520 0Z" fill="#fff"/>
    <path d="M560 104C640 132 720 126 780 100" fill="none" stroke="var(--lime)" stroke-width="3"/>
    <path d="M520 390C600 410 700 400 780 380" fill="none" stroke="var(--lime-deep)" stroke-width="3"/>
  </svg>

  <!-- LEFT PANEL -->
  <section class="panel panel--left">
    <h2 class="section-title">Why <span>Choose Us</span></h2>

    <div class="feature" style="top:66px">
      <svg class="feature__icon" viewBox="0 0 20 20"><circle cx="10" cy="10" r="10" fill="var(--lime-deep)"/><path d="M5.5 10.5l3 3 6-6.5" fill="none" stroke="#fff" stroke-width="2"/></svg>
      <h3 class="feature__title">QUALITY</h3>
      <p class="feature__text">Our goal is to enhance your property and achieve the results you are looking for. We appreciate the trust placed in us to deliver a quality job that meets your expectations...</p>
    </div>
    <div class="feature" style="top:148px">
      <svg class="feature__icon" viewBox="0 0 20 20"><rect x="2" y="7" width="16" height="7" rx="3" fill="var(--lime-deep)"/></svg>
      <h3 class="feature__title">PROFESSIONALISM</h3>
      <p class="feature__text">Larkmore only use quality staff and materials that are “fit for purpose”. We keep a professional approach to every job ensuring all agreed tasks are completed and accounted...</p>
    </div>
    <div class="feature" style="top:233px">
      <svg class="feature__icon" viewBox="0 0 20 20"><circle cx="10" cy="10" r="10" fill="var(--lime-deep)"/><path d="M6 9h2v6H6zM9 15V9l2-4c1.5 0 1.5 1.5 1 3h3v3l-1.5 4z" fill="#fff"/></svg>
      <h3 class="feature__title">PRIDE</h3>
      <p class="feature__text">We take pride in our family approach and care we bring to your loved ones belongings. Whether it is simple house clearing, house repairs or larger renovations your...</p>
    </div>
    <div class="feature" style="top:318px">
      <svg class="feature__icon" viewBox="0 0 20 20"><path d="M10 1a6 6 0 0 0-6 6c0 4.5 6 11 6 11s6-6.5 6-11a6 6 0 0 0-6-6z" fill="var(--lime-deep)"/><circle cx="10" cy="7" r="2.2" fill="#fff"/></svg>
      <h3 class="feature__title">AREAS SERVICED</h3>
      <p class="feature__text">Specialising in Melbourne CBD and suburbs including: Coburg, Falkner, Campbellfield, Craigieburn, St. Kilda, Brighton, Caulfield, Hawthorn, Heidelberg, Watsonia...</p>
    </div>

    <div role="img" aria-label="Photo: a care worker shaking hands with an elderly couple in a bright living room" style="position:absolute;left:0;top:412px;width:260px;height:163px;background:linear-gradient(135deg,#eef0ea,#d9dccf 55%,#b8ad9c)"></div>
    <div class="footer footer--purple">www.larkmore.com.au</div>
  </section>

  <!-- MIDDLE PANEL -->
  <section class="panel panel--mid">
    <svg style="position:absolute;left:44px;top:22px" width="172" height="172" aria-hidden="true"><circle cx="86" cy="86" r="85" fill="#e9e6f0"/></svg>
    <div role="img" aria-label="Photo: smiling senior couple sitting on a wooden bench outside a brick house" style="position:absolute;left:55px;top:33px;width:150px;height:150px;border-radius:50%;background:linear-gradient(160deg,#c9a58b,#9c8c80 50%,#7e8ba0)"></div>

    <div class="quote">
      <div class="quote__mark">“</div>
      <p class="quote__text">Check out Larkmore if you are in need of home, building, and storage units clean out services that will suit your needs. They also handle estate sales and are always available on time.</p>
      <div class="quote__name"><b>DANIEL <small>CUSTOMER</small></b></div>
    </div>

    <div class="contact-brand">
      <span class="brand-dot"></span>
      <div class="brand">LARKMORE</div>
    </div>
    <p class="enquire">If you have any queries,<strong><em>Get in touch</em> with us</strong></p>
    <div class="icons" aria-hidden="true">
      <svg viewBox="0 0 14 14"><circle cx="7" cy="7" r="7" fill="var(--blue)"/><path d="M7 3a2.5 2.5 0 0 0-2.5 2.5C4.5 7.5 7 11 7 11s2.5-3.5 2.5-5.5A2.5 2.5 0 0 0 7 3z" fill="#fff"/></svg>
      <svg viewBox="0 0 14 14"><circle cx="7" cy="7" r="7" fill="var(--blue)"/><path d="M4.5 3.5l1.5 0 .8 2-1 .8a5 5 0 0 0 2 2l.8-1 2 .8v1.5c-3 .5-6.5-3-6.1-6.1z" fill="#fff"/></svg>
      <svg viewBox="0 0 14 14"><circle cx="7" cy="7" r="7" fill="var(--blue)"/><rect x="4" y="4" width="6" height="6" fill="#fff"/></svg>
      <svg viewBox="0 0 14 14"><circle cx="7" cy="7" r="7" fill="var(--blue)"/><circle cx="7" cy="7" r="3.5" fill="none" stroke="#fff"/><path d="M3.5 7h7M7 3.5v7" stroke="#fff" stroke-width=".8"/></svg>
    </div>
    <p class="contact-lines">PO Box 204, Northbrook 3100<br>0400 123 456<br>0400 654 321<br>info@larkmore.com.au</p>
    <div class="footer footer--lime">www.larkmore.com.au</div>
  </section>

  <!-- RIGHT PANEL -->
  <section class="panel panel--right">
    <div class="right-brand">
      <span class="brand-dot"></span>
      <div class="brand">LARKMORE</div>
    </div>
    <div role="img" aria-label="Photo: bucket of colourful cleaning supplies, spray bottles, cloths and gloves" style="position:absolute;left:0;top:128px;width:260px;height:262px;background:linear-gradient(160deg,#dce9f4,#9fc7e6 40%,#5aa9d8 65%,#8dc74a)"></div>
    <p class="tagline">WE’RE HERE TO HELP</p>
    <h1 class="headline"><span>DECEASED ESTATE</span><strong>CLEANUPS</strong></h1>
    <p class="intro">At Larkmore our goal is to ease your worries and help you with your journey in preparing your house for rental or resale.</p>
    <div class="footer footer--purple">www.larkmore.com.au</div>
  </section>
</main>
</body>
</html>
```